Logo is done, need templates now

I want to be able to have an email template, same for word documents, powerpoint etc. I have the logo, now I need all the pieces for appearance in correspondence and marketing

Target Market(s)

Professional Advisors and Wealthy Clients

Font styles to use
Serif

Requirements
Must have
• I want to be able to do word documents and email them with letterhead. I need great email signatures. I need similar formatting for the word documents to be flexible to add to powerpoint and other presentations.

```html
<!DOCTYPE html>
<html lang="en">
<head>
<meta charset="UTF-8">
<title>Quietwater Capital — Letterhead</title>
<link rel="stylesheet" href="https://fonts.googleapis.com/css2?family=Libre+Bodoni:wght@400&display=swap">
<style>
  :root {
    --gold-dark: #8a5f34;
    --gold-mid: #c49560;
    --gold-light: #f3cd95;
    --gold-deep: #a87135;
    --gold-ink: #b4834d;
    --paper: #ffffff;
    --footer-ink: #ffffff;
    --gold-gradient: linear-gradient(90deg, var(--gold-dark) 0%, var(--gold-mid) 25%, var(--gold-light) 47%, var(--gold-mid) 75%, var(--gold-deep) 100%);
  }
  * { box-sizing: border-box; margin: 0; padding: 0; }
  html, body {
    width: 835px;
    height: 1200px;
    overflow: hidden;
    background: var(--paper);
  }
  .letterhead {
    position: relative;
    width: 835px;
    height: 1200px;
    background: var(--gold-gradient);
    font-family: "Libre Bodoni", "Bodoni Moda", serif;
  }
  .letterhead__sheet {
    position: absolute;
    left: 13px;
    top: 13px;
    width: 810px;
    height: 1068px;
    background: var(--paper);
  }
  .brand {
    position: absolute;
    top: 100px;
    left: 0;
    width: 100%;
    text-align: center;
  }
  .brand__name {
    display: inline-block;
    color: var(--gold-ink);
    font-size: 17px;
    font-weight: 400;
    letter-spacing: 0.32em;
    text-transform: uppercase;
    padding-left: 0.32em;
  }
  .letterhead__footer {
    position: absolute;
    left: 35px;
    top: 1099px;
    color: var(--footer-ink);
    font-size: 18px;
    line-height: 24.5px;
    font-weight: 400;
    list-style: none;
  }
</style>
</head>
<body>
  <main class="letterhead">
    <section class="letterhead__sheet">
      <header class="brand">
        <span class="brand__name">Quietwater Capital</span>
      </header>
    </section>
    <ul class="letterhead__footer">
      <li class="contact contact--phone">Phone number</li>
      <li class="contact contact--web">Website</li>
      <li class="contact contact--address">Adress</li>
    </ul>
  </main>
</body>
</html>
```